Fireworks company

COLORFUL design, incorporating logo (attached).
Information to be included:
PO BOX 4829
Marlow Vale 3891
Ph 03 5461 8237
Fax 03 5387 9216
Email sales@brindarockets.com.au
Web www.brindarockets.com.au

Check out our website for more inspiration? :-)

```html
<!DOCTYPE html>
<html lang="en">
<head>
<meta charset="utf-8">
<title>Brinda Rockets Letterhead</title>
<link href="https://fonts.googleapis.com/css2?family=Cabin:wght@400;700&display=swap" rel="stylesheet">
<style>
  :root {
    --orange: #f4821f;
    --paper: #ffffff;
    --ink: #111111;
    --spark-cream: #fbe9b4;
    --spark-rose: #f2b7a0;
  }
  html, body {
    margin: 0;
    padding: 0;
    overflow: hidden;
  }
  body {
    width: 880px;
    height: 1200px;
    font-family: "Cabin", "Gill Sans", sans-serif;
  }
  .letterhead {
    position: relative;
    width: 880px;
    height: 1200px;
    background: var(--orange);
    overflow: hidden;
  }
  .sheet {
    position: absolute;
    left: 9px;
    top: 7px;
    right: 9px;
    bottom: 93px;
    background: var(--paper);
  }
  .header-tab {
    position: absolute;
    left: 0;
    top: 62px;
    width: 18px;
    height: 68px;
    background: var(--orange);
  }
  .header-band {
    position: absolute;
    left: 334px;
    top: 69px;
    right: 0;
    height: 54px;
    background: var(--orange);
  }
  .brand {
    position: absolute;
    left: 50px;
    top: 62px;
    display: flex;
    align-items: center;
    gap: 12px;
  }
  .brand-name {
    font-family: "Cabin", "Gill Sans", sans-serif;
    font-weight: 700;
    font-size: 38px;
    line-height: 1;
    color: var(--orange);
    letter-spacing: 0.5px;
  }
  .brand-dot {
    width: 22px;
    height: 22px;
    border-radius: 50%;
    background: var(--orange);
  }
  .spark-decoration {
    position: absolute;
    left: 0;
    top: 378px;
    width: 470px;
    height: 352px;
    background: radial-gradient(ellipse at 45% 55%, rgba(251, 233, 180, 0.75) 0%, rgba(242, 183, 160, 0.35) 45%, rgba(255, 255, 255, 0) 72%);
  }
  .contact-card {
    position: absolute;
    left: 136px;
    top: 1113px;
    width: 608px;
    height: 78px;
    background: var(--paper);
    border-radius: 7px;
    text-align: center;
    color: var(--ink);
  }
  .contact-title {
    margin: 6px 0 4px;
    font-weight: 700;
    font-size: 15px;
    text-decoration: underline;
  }
  .contact-line {
    margin: 0 0 4px;
    font-size: 14.5px;
  }
</style>
</head>
<body>
  <div class="letterhead">
    <div class="sheet"></div>
    <div class="header-tab"></div>
    <div class="header-band"></div>

    <div class="brand">
      <span class="brand-name">Brinda Rockets</span>
      <span class="brand-dot"></span>
    </div>

    <div class="spark-decoration" role="img" aria-label="Faint decorative illustration of cream and pink firework bursts"></div>

    <div class="contact-card">
      <p class="contact-title">Brinda Rockets:</p>
      <p class="contact-line">PO BOX 4829, Marlow Vale 3891, Ph.:-03 5461 8237, Fax.:- 03 5387 9216</p>
      <p class="contact-line">Email.:- sales@brindarockets.com.au, Web.: www.brindarockets.com.au</p>
    </div>
  </div>
</body>
</html>
```